Smile club flyer design

I am launching an office smile club and would like a design that sits my branding and that is appealing to customers. I have a design (I need a new one) that has all the information.
My website is maplecrestdentalcarewv.com
Brand color is green. The design can be any color

Target Market(s)

Ages 30+

Industry/Entity Type

Dental

Font styles to use
Serif

Requirements
Must have
• Appealing to patients

```html
<!DOCTYPE html>
<html lang="en">
<head>
<meta charset="utf-8">
<title>Maplecrest Dental Care – Smile Club Membership</title>
<link href="https://fonts.googleapis.com/css2?family=Playfair+Display:wght@400;600;700;800&family=Montserrat:wght@400;500;600;700&display=swap" rel="stylesheet">
<style>
  :root{
    --stage:#8a8a8a;
    --mint:#a9e6da;
    --card:#c6f0e7;
    --teal:#1fb3a1;
    --teal-dark:#149584;
    --brand-green:#138a4a;
    --ink:#1b2a2a;
    --white:#ffffff;
  }
  *{box-sizing:border-box;margin:0;padding:0}
  html,body{width:1021px;height:1200px;overflow:hidden;background:var(--stage)}
  .flyer{position:absolute;left:122px;top:49px;width:771px;height:1038px;background:var(--mint);overflow:hidden;font-family:"Montserrat",sans-serif;color:var(--ink)}
  .foliage{position:absolute;inset:0;background:
      radial-gradient(ellipse 260px 200px at 40px 60px,rgba(255,255,255,.22),transparent 70%),
      radial-gradient(ellipse 300px 240px at 740px 120px,rgba(255,255,255,.2),transparent 70%),
      radial-gradient(ellipse 260px 260px at 80px 980px,rgba(60,170,150,.18),transparent 70%),
      radial-gradient(ellipse 300px 260px at 700px 560px,rgba(60,170,150,.15),transparent 70%)}
  .center{position:absolute;left:0;width:100%;text-align:center;white-space:nowrap}
  .brand-name{top:82px;font-family:"Playfair Display",serif;font-weight:800;font-size:64px;color:var(--brand-green);letter-spacing:-.5px;line-height:1}
  .brand-sub{top:160px;font-family:"Playfair Display",serif;font-weight:700;font-size:24px;letter-spacing:7px;color:var(--brand-green)}
  .brand-sub::before,.brand-sub::after{content:"";display:inline-block;width:46px;height:3px;background:var(--brand-green);vertical-align:middle;margin:0 14px}
  .intro{top:222px;font-family:"Playfair Display",serif;font-size:38px;letter-spacing:4px}
  .title{top:270px;font-family:"Playfair Display",serif;font-weight:600;font-size:86px;letter-spacing:2px;color:var(--teal);line-height:1}
  .subtitle{top:356px;font-family:"Playfair Display",serif;font-weight:800;font-size:38px;letter-spacing:5px}
  .tagline{top:412px;font-size:19px;font-weight:500;letter-spacing:.5px}
  .plan{position:absolute;width:202px;background:var(--card);border-radius:10px;box-shadow:0 6px 14px rgba(20,110,95,.25);padding-bottom:12px}
  .plan-tab{background:var(--teal);color:var(--white);text-align:center;border-radius:10px 10px 0 0;padding:8px 4px 6px}
  .plan-name{font-family:"Playfair Display",serif;font-weight:600;font-size:21px;letter-spacing:1px;line-height:1.1}
  .plan-type{font-size:11px;letter-spacing:1.5px;font-weight:500}
  .price{text-align:center;color:var(--teal);font-family:"Playfair Display",serif;font-weight:600;font-size:46px;line-height:1;margin-top:8px}
  .price sup{font-size:20px;vertical-align:top;position:relative;top:6px}
  .per{text-align:center;font-size:11px;letter-spacing:1.5px;font-weight:600;margin-bottom:9px}
  .features{list-style:none;padding:0 10px}
  .features li{position:relative;padding-left:14px;font-size:10px;line-height:1.3;margin-bottom:8px}
  .features li:last-child{margin-bottom:0}
  .features li::before{content:"";position:absolute;left:2px;top:4px;width:6px;height:6px;border-radius:50%;background:var(--teal)}
  .plan-core{left:62px;top:468px;min-height:254px}
  .plan-bright{left:278px;top:468px;min-height:246px}
  .plan-total{left:495px;top:468px;min-height:254px}
  .plan-refresh{left:495px;top:754px;min-height:221px}
  .financing{position:absolute;left:30px;width:450px;text-align:center;white-space:nowrap}
  .fin-head{top:752px;font-family:"Playfair Display",serif;font-size:20px;letter-spacing:.5px}
  .partners{top:784px;display:flex;justify-content:center;align-items:center;gap:14px;font-family:"Playfair Display",serif;font-weight:700;font-size:30px;line-height:1.2}
  .partners .divider{width:2px;height:30px;background:var(--ink)}
  .plans-head{top:832px;font-family:"Playfair Display",serif;font-size:20px;letter-spacing:.5px}
  .fee{top:868px}
  .fee span{display:inline-block;background:var(--teal);color:var(--white);font-size:11px;padding:5px 14px;border-radius:12px}
  .join{top:906px;font-family:"Playfair Display",serif;font-weight:800;font-size:26px;color:var(--teal-dark);letter-spacing:.5px}
  .phone{top:944px;display:flex;justify-content:center;align-items:center;gap:10px;font-size:30px;font-weight:500}
</style>
</head>
<body>
<main class="flyer">
  <div class="foliage" role="img" aria-label="Faint leafy branch decoration in soft mint tones"></div>

  <div class="center brand-name">Maplecrest</div>
  <div class="center brand-sub">DENTAL CARE</div>

  <div class="center intro">Introducing</div>
  <h1 class="center title">SMILE CLUB</h1>
  <div class="center subtitle">MEMBERSHIP</div>
  <p class="center tagline">AFFORDABLE DENTAL CARE – NO INSURANCE REQUIRED</p>

  <section class="plan plan-core">
    <div class="plan-tab"><div class="plan-name">CORE CARE</div><div class="plan-type">PREVENTIVE</div></div>
    <div class="price"><sup>$</sup>39</div>
    <div class="per">MONTH</div>
    <ul class="features">
      <li>Comprehensive Annual Exam</li>
      <li>2 Professional Cleanings per Year</li>
      <li>Routine Bitewing X-rays</li>
      <li>10% Savings on Treatment</li>
    </ul>
  </section>

  <section class="plan plan-bright">
    <div class="plan-tab"><div class="plan-name">BRIGHT</div><div class="plan-type">COSMETIC</div></div>
    <div class="price"><sup>$</sup>59</div>
    <div class="per">MONTH</div>
    <ul class="features">
      <li>Annual In-Office Whitening (Top &amp; Bottom)</li>
      <li>Custom Whitening Trays</li>
      <li>15% Savings on Elective Treatment</li>
    </ul>
  </section>

  <section class="plan plan-total">
    <div class="plan-tab"><div class="plan-name">TOTAL SMILE</div><div class="plan-type">PERIODONTAL</div></div>
    <div class="price"><sup>$</sup>89</div>
    <div class="per">MONTH</div>
    <ul class="features">
      <li>3-4 Perio Maintenance Visits per Year</li>
      <li>1 Comprehensive Exam</li>
      <li>Diagnostic X-rays</li>
      <li>15% Savings on Restorative &amp; Elective Care</li>
    </ul>
  </section>

  <section class="plan plan-refresh">
    <div class="plan-tab"><div class="plan-name">SMILE</div><div class="plan-type">REFRESH PACKAGE</div></div>
    <div class="price"><sup>$</sup>499</div>
    <div class="per">MONTH</div>
    <ul class="features">
      <li>Cleaning + Comprehensive Exam + Whitening</li>
      <li>Limited Time Offer</li>
    </ul>
  </section>

  <div class="financing fin-head">FLEXIBLE FINANCING FOR TREATMENT</div>
  <div class="financing partners"><span>HealthPay</span><span class="divider"></span><span>plumline</span></div>
  <div class="financing plans-head">PAYMENT PLANS AVAILABLE</div>
  <div class="financing fee"><span>*$49 Lifetime Activation Fee (Non-Refundable)</span></div>
  <div class="financing join">JOIN SMILE CLUB TODAY!</div>
  <div class="financing phone">
    <svg width="26" height="26" viewBox="0 0 24 24" aria-hidden="true"><path fill="#1b2a2a" d="M6.6 10.8a15.1 15.1 0 0 0 6.6 6.6l2.2-2.2c.3-.3.7-.4 1-.2 1.1.4 2.3.6 3.6.6.6 0 1 .4 1 1V20c0 .6-.4 1-1 1A17 17 0 0 1 3 4c0-.6.4-1 1-1h3.5c.6 0 1 .4 1 1 0 1.3.2 2.5.6 3.6.1.3 0 .7-.2 1z"/></svg>
    <span>555-210-7800</span>
  </div>
</main>
</body>
</html>
```